Bingo Night

Willowmere Terraces is an Assisted Living Facility. We have 34 residents currently living in our facility. We provide care for elderly patients that need a slightly higher level of care than what can be provided at home. We are sending out this invitation to people in the surrounding community for Bingo night March 19, 2014 @ 6:00pm. The colors we would like to use are gold & maroon. Our address is 2947 W 38th St Tulsa, OK 74107. 918-562-3049. Also, the phrase "open to the public" should be incorporated on both sides.
Updates

Target Market(s)

Men and women between the ages of 50-90 years old.

Industry/Entity Type

Community

Font styles to use
Serif
Script

Requirements
Must have
• At least 4 pictures provided, our address, time of event, and phone number.

```html
<!DOCTYPE html>
<html lang="en">
<head>
<meta charset="utf-8">
<title>Bingo Night – Willowmere Terraces</title>
<link rel="stylesheet" href="https://fonts.googleapis.com/css2?family=Fjalla+One&family=Norican&display=swap">
<style>
  :root {
    --frame-olive: #b3b23a;
    --frame-olive-dark: #9d9c2c;
    --panel-magenta: #8c1869;
    --panel-magenta-light: #a3287f;
    --text-olive: #8f8d26;
    --text-white: #ffffff;
    --seal-green: #1e3b22;
    --seal-text: #a09e2e;
  }
  * { margin: 0; padding: 0; box-sizing: border-box; }
  html, body { width: 1200px; height: 930px; overflow: hidden; background: #fff; }
  .invitation {
    position: relative;
    width: 1200px;
    height: 930px;
    overflow: hidden;
  }
  .frame-pattern {
    position: absolute;
    inset: 0;
    background: linear-gradient(135deg, var(--frame-olive), var(--frame-olive-dark));
  }
  .panel {
    position: absolute;
    left: 31px; top: 29px;
    width: 1139px; height: 869px;
    background: radial-gradient(ellipse at 50% 45%, var(--panel-magenta-light), var(--panel-magenta) 75%);
  }
  .presenter {
    position: absolute;
    top: 70px; left: 0; width: 100%;
    text-align: center;
    font-family: "Fjalla One", sans-serif;
    font-size: 33px;
    color: var(--text-olive);
    letter-spacing: 0.5px;
  }
  .title {
    position: absolute;
    left: 0; width: 100%;
    text-align: center;
    font-family: "Norican", cursive;
    font-weight: 400;
    font-size: 200px;
    color: var(--text-white);
    text-shadow: 5px 6px 0 var(--text-olive);
    line-height: 1;
  }
  .title-bingo { top: 180px; transform: translateX(-55px) rotate(-4deg); }
  .title-night { top: 395px; transform: translateX(0) rotate(-4deg); }
  .seal { position: absolute; width: 190px; height: 190px; }
  .seal-time { left: 90px; top: 362px; }
  .seal-public { left: 925px; top: 362px; }
  .seal-label {
    position: absolute; inset: 0;
    display: flex; align-items: center; justify-content: center;
    text-align: center;
    font-family: "Norican", cursive;
    color: var(--seal-text);
    transform: rotate(-8deg);
  }
  .seal-time .seal-label { font-size: 92px; }
  .seal-time .seal-label small { font-size: 44px; align-self: flex-start; margin-top: 44px; }
  .seal-public .seal-label { font-size: 36px; line-height: 1.05; }
  .event-date {
    position: absolute;
    top: 726px; left: 0; width: 100%;
    text-align: center;
    font-family: "Fjalla One", sans-serif;
    font-size: 54px;
    color: var(--text-white);
  }
  .venue-contact {
    position: absolute;
    top: 810px; left: 0; width: 100%;
    text-align: center;
    font-family: "Fjalla One", sans-serif;
    font-size: 35px;
    color: var(--text-olive);
  }
</style>
</head>
<body>
<main class="invitation">
  <div class="frame-pattern" role="img" aria-label="Olive green border with a repeating swirl pattern"></div>
  <div class="panel" role="img" aria-label="Magenta background with a subtle swirl texture"></div>

  <p class="presenter">Willowmere Terraces presents</p>

  <h1 class="title title-bingo">Bingo</h1>
  <h1 class="title title-night">night</h1>

  <div class="seal seal-time">
    <svg width="190" height="190" viewBox="-95 -95 190 190" aria-hidden="true">
      <g fill="var(--seal-green)">
        <rect x="-66" y="-66" width="132" height="132" rx="6"/>
        <rect x="-66" y="-66" width="132" height="132" rx="6" transform="rotate(10)"/>
        <rect x="-66" y="-66" width="132" height="132" rx="6" transform="rotate(20)"/>
        <rect x="-66" y="-66" width="132" height="132" rx="6" transform="rotate(30)"/>
        <rect x="-66" y="-66" width="132" height="132" rx="6" transform="rotate(40)"/>
        <rect x="-66" y="-66" width="132" height="132" rx="6" transform="rotate(50)"/>
        <rect x="-66" y="-66" width="132" height="132" rx="6" transform="rotate(60)"/>
        <rect x="-66" y="-66" width="132" height="132" rx="6" transform="rotate(70)"/>
        <rect x="-66" y="-66" width="132" height="132" rx="6" transform="rotate(80)"/>
      </g>
    </svg>
    <p class="seal-label">6<small>pm</small></p>
  </div>

  <div class="seal seal-public">
    <svg width="190" height="190" viewBox="-95 -95 190 190" aria-hidden="true">
      <g fill="var(--seal-green)">
        <rect x="-66" y="-66" width="132" height="132" rx="6"/>
        <rect x="-66" y="-66" width="132" height="132" rx="6" transform="rotate(10)"/>
        <rect x="-66" y="-66" width="132" height="132" rx="6" transform="rotate(20)"/>
        <rect x="-66" y="-66" width="132" height="132" rx="6" transform="rotate(30)"/>
        <rect x="-66" y="-66" width="132" height="132" rx="6" transform="rotate(40)"/>
        <rect x="-66" y="-66" width="132" height="132" rx="6" transform="rotate(50)"/>
        <rect x="-66" y="-66" width="132" height="132" rx="6" transform="rotate(60)"/>
        <rect x="-66" y="-66" width="132" height="132" rx="6" transform="rotate(70)"/>
        <rect x="-66" y="-66" width="132" height="132" rx="6" transform="rotate(80)"/>
      </g>
    </svg>
    <p class="seal-label">Open<br>to the<br>public!</p>
  </div>

  <p class="event-date">MARCH 19, 2014</p>
  <p class="venue-contact">2947 W 38th ST TULSA, OK 74107 - 918-562-3049</p>
</main>
</body>
</html>
```